Consulting, Investors, Joint Venture Website

Founded in April 2018, Marendo Advisers Limited (MAL) is an advisory consulting firm specializing in engaging investors in business ventures in Tanzania.
With extensive experience in construction, energy, oil and gas and the legal professions, our team assembles our expertise that allows foreign investors to set foot and flourish in the Tanzanian market.
MAL is locally owned, founded and registered. Our shareholders are cultured Tanzanian citizens with extensive corporate experience in South Africa, Tanzania, United Kingdom and the United States.

Our mission is to provide responsive and unrivalled professional advice from learned and experienced professionals versed in the local market, with an understanding of the cultural and logistical challenges faced by foreign investors.

Our vision is to provide a complete investor’s package that initiates with company registration, compliance and documentation services and ultimately operational facilitation services.

Target Market(s)

Foreign Investors, International companies

Industry/Entity Type

Business Consultant

Number of Pages Required

5+ page

Requirements
Must have
• It will be 5 pages - Home, About Us, Services, Portfolio, Contact Us
Nice to have
• if it can look like https://www.vq-sample.com/
• or https://www.torvell.com or http://www.bramwickpoint.com/

```html
<!DOCTYPE html>
<html lang="en">
<head>
<meta charset="utf-8">
<title>Marendo Advisers Limited</title>
<link href="https://fonts.googleapis.com/css2?family=Lato:wght@400;700;900&display=swap" rel="stylesheet">
<style>
:root{
  --orange:#f7a11a;
  --blue:#0d4fa1;
  --blue-dark:#0a3f86;
  --blue-soft:#cddbf0;
  --ink:#333;
  --muted:#666;
  --dark:#262626;
  --tile:#e8e8e8;
  --white:#fff;
}
*{box-sizing:border-box;margin:0;padding:0}
html,body{width:1200px;height:4580px;overflow:hidden}
body{font-family:'Lato',sans-serif;color:var(--ink);position:relative;background:#fff}
.abs{position:absolute}
.btn{position:absolute;display:flex;align-items:center;justify-content:center;border-radius:30px;font-size:17px;font-weight:700;text-transform:uppercase;letter-spacing:.3px;white-space:nowrap}
.btn-orange{background:var(--orange);color:#fff}
.btn-blue{background:var(--blue);color:#fff}
.ph{position:absolute}
.h2{font-size:38px;font-weight:900;white-space:nowrap}
.rule{position:absolute;height:3px;width:62px;background:var(--orange)}
.txt{font-size:14.5px;line-height:1.7;color:var(--muted)}

/* top bar */
.topbar{top:0;left:0;width:1200px;height:55px;background:var(--orange);color:#fff;font-size:15px}
.topbar .item{position:absolute;top:17px;display:flex;align-items:center;gap:8px}
.social{position:absolute;display:flex;gap:12px}
.social span{display:block;border-radius:50%}

/* header */
.header{top:55px;left:0;width:1200px;height:113px;background:#fff}
.brand{position:absolute;left:78px;top:32px;display:flex;align-items:center;gap:12px}
.brand .mark{width:44px;height:44px;background:var(--blue)}
.brand .name{font-size:25px;font-weight:900;color:var(--blue);letter-spacing:1px;line-height:1}
.nav{position:absolute;top:43px;left:506px;display:flex;gap:56px;font-size:16px;color:#555}
.search{position:absolute;left:1078px;top:32px;width:44px;height:44px;border-radius:50%;background:var(--blue)}

/* hero */
.hero{top:168px;left:0;width:1200px;height:574px;background:linear-gradient(90deg,#1a1a1f 0%,#2a2a33 50%,#3b3a40 100%)}
.hero .title{left:80px;top:120px;font-size:44px;font-weight:900;color:var(--orange);white-space:nowrap}
.hero .sub{left:80px;top:185px;font-size:31px;color:#fff;font-weight:700}
.hero .lead{left:80px;top:232px;font-size:14px;color:#ddd;line-height:1.75}
.arrowbox{position:absolute;width:52px;height:52px;border-radius:50%;background:#333;border:2px solid #666;display:flex;align-items:center;justify-content:center}

/* services tiles */
.tile{position:absolute;width:230px;height:134px;background:var(--tile);border:1px solid #d6d6d6;text-align:center}
.tile .ic{width:52px;height:52px;margin:18px auto 10px;background:#cfcfcf;border-radius:6px}
.tile .lb{font-size:17px;color:var(--orange)}

/* band */
.band{top:1618px;left:0;width:1200px;height:147px;background:linear-gradient(90deg,#2b2b2b,#3d3d3d 60%,#2b2b2b)}

/* news */
.card-date{position:absolute;background:var(--orange);color:#fff;font-size:18px;font-weight:700;padding:8px 16px}
.news-title{font-size:17px;font-weight:700;color:var(--orange);white-space:nowrap}
.readmore{font-size:14px;font-weight:700;color:var(--ink);text-transform:uppercase}

/* callback */
.callback{top:3221px;left:0;width:1200px;height:314px;background:var(--blue)}
.field{position:absolute;height:58px;background:rgba(255,255,255,.35);color:#fff;font-size:15px;padding:18px 14px}

/* clients */
.quote{position:absolute;width:322px;height:170px;background:#fff;box-shadow:0 2px 10px rgba(0,0,0,.15);padding:24px 28px 0 50px;font-size:14.5px;line-height:1.75;color:var(--muted)}
.quote .q{position:absolute;left:16px;top:14px;font-size:40px;color:var(--orange);font-weight:900;line-height:1}
.avatar{position:absolute;width:100px;height:100px;border-radius:50%;background:linear-gradient(#d9dde3,#b9c0c9);border:4px solid #fff;box-shadow:0 1px 5px rgba(0,0,0,.2)}
.cname{position:absolute;font-size:20px;color:var(--orange);font-weight:700}
.crole{position:absolute;font-size:14px;color:var(--muted)}

/* footer */
.footer{top:4152px;left:0;width:1200px;height:382px;background:linear-gradient(90deg,#161616,#2a2a2a 50%,#1b1b1b);color:#fff}
.footer h4{position:absolute;font-size:20px;font-weight:700;color:var(--orange)}
.footer .col{position:absolute;font-size:14px;line-height:2.3;color:#eee}
.bottombar{top:4534px;left:0;width:1200px;height:46px;background:var(--orange);color:#fff;font-size:14px;text-align:center;line-height:46px}
</style>
</head>
<body>

<!-- top bar -->
<div class="abs topbar">
  <div class="item" style="left:78px">
    <svg width="16" height="16" viewBox="0 0 24 24"><path fill="#fff" d="M6.6 10.8a15 15 0 0 0 6.6 6.6l2.2-2.2c.3-.3.7-.4 1-.2 1.1.4 2.3.6 3.6.6.6 0 1 .4 1 1V20c0 .6-.4 1-1 1A17 17 0 0 1 3 4c0-.6.4-1 1-1h3.5c.6 0 1 .4 1 1 0 1.3.2 2.5.6 3.6.1.3 0 .7-.2 1z"/></svg>
    555-014-2790
  </div>
  <div class="item" style="left:243px">
    <svg width="18" height="14" viewBox="0 0 18 14"><rect x="0.5" y="0.5" width="17" height="13" fill="#fff"/><path d="M1 1l8 6 8-6" stroke="#f7a11a" stroke-width="1.5" fill="none"/></svg>
    info@marendo-advisers.com
  </div>
  <div class="social" style="left:1012px;top:13px">
    <span style="width:28px;height:28px;background:var(--blue)"></span>
    <span style="width:28px;height:28px;background:var(--blue)"></span>
    <span style="width:28px;height:28px;background:var(--blue)"></span>
  </div>
</div>

<!-- header -->
<header class="abs header">
  <div class="brand"><div class="mark"></div><div class="name">MARENDO ADVISERS</div></div>
  <nav class="nav"><span>Home</span><span>About Us</span><span>Services</span><span>Portfolio</span><span>Contact</span></nav>
  <div class="search"><svg width="44" height="44" viewBox="0 0 44 44"><circle cx="20" cy="20" r="7" stroke="#fff" stroke-width="2.5" fill="none"/><line x1="25" y1="25" x2="30" y2="30" stroke="#fff" stroke-width="2.5"/></svg></div>
</header>

<!-- hero -->
<section class="abs hero">
  <div class="ph" role="img" aria-label="Evening city skyline behind the hero" style="left:0;top:0;width:1200px;height:574px;background:linear-gradient(180deg,rgba(60,60,70,.4),rgba(20,20,25,.7) 70%,rgba(70,55,40,.5))"></div>
  <div class="ph" role="img" aria-label="Businesswoman holding a red folder" style="left:740px;top:0;width:380px;height:574px;background:linear-gradient(180deg,#4a4a50 0%,#6a6a70 40%,#2a2a2e 75%,#1e1e22 100%);opacity:.85"></div>
  <div class="abs title">Marendo Advisers Limited</div>
  <div class="abs sub">Solution &amp; Consulting</div>
  <div class="abs lead">Lorem Ipsum is simply dummy text of the printing and typesetting industry.<br>Lorem Ipsum has been the industry's standard dummy text ever since the 1500s.</div>
  <div class="btn" style="left:80px;top:312px;width:184px;height:56px;border:2px solid #fff;color:#fff">Our Services</div>
  <div class="btn btn-orange" style="left:278px;top:312px;width:184px;height:56px">Contact Us</div>
  <div class="arrowbox" style="left:-18px;top:260px"><svg width="12" height="14"><path d="M9 1L2 7l7 6" stroke="#fff" stroke-width="2" fill="none"/></svg></div>
  <div class="arrowbox" style="left:1146px;top:260px"><svg width="12" height="14"><path d="M3 1l7 6-7 6" stroke="#fff" stroke-width="2" fill="none"/></svg></div>
</section>

<!-- services intro -->
<section>
  <div class="rule" style="left:78px;top:800px"></div>
  <h2 class="abs h2" style="left:78px;top:812px;color:var(--blue)">Our Services</h2>
  <p class="abs txt" style="left:78px;top:880px;width:520px">Lorem Ipsum is simply dummy text of the printing and typesetting industry. Lorem Ipsum has been the industry's standard dummy text ever since the 1500s, when an unknown printer took a galley of type and scrambled it make a1500s, when unknown printer took a galley of type and scrambled it make a type specimen book.</p>
  <div class="btn btn-orange" style="left:78px;top:1032px;width:146px;height:56px">Ream More</div>

  <div class="tile" style="left:650px;top:804px"><div class="ic" role="img" aria-label="Construction icon"></div><div class="lb">Construction</div></div>
  <div class="tile" style="left:892px;top:804px"><div class="ic" role="img" aria-label="Energy bulb icon"></div><div class="lb">eEnergy</div></div>
  <div class="tile" style="left:650px;top:956px"><div class="ic" role="img" aria-label="Oil rig icon"></div><div class="lb">Oil and gas</div></div>
  <div class="tile" style="left:892px;top:956px"><div class="ic" role="img" aria-label="Legal professional icon"></div><div class="lb">The legal professions</div></div>
</section>

<!-- services feature -->
<section>
  <div class="ph" role="img" aria-label="Soft light-blue decorative backdrop" style="left:0;top:1140px;width:420px;height:450px;background:radial-gradient(ellipse at 45% 45%,var(--blue-soft) 0%,rgba(205,219,240,.6) 50%,rgba(255,255,255,0) 75%)"></div>
  <div class="ph" role="img" aria-label="Business team meeting around a laptop" style="left:80px;top:1198px;width:456px;height:318px;background:linear-gradient(135deg,#e9edf2,#b9c3cf 60%,#8c97a6);border:8px solid #fff;box-shadow:0 2px 12px rgba(0,0,0,.2)"></div>
  <div class="rule" style="left:1060px;top:1200px"></div>
  <h2 class="abs h2" style="right:78px;top:1212px;color:var(--orange)">Our Services</h2>
  <p class="abs txt" style="right:78px;top:1276px;width:500px;text-align:right">Lorem Ipsum is simply dummy text of the printing and typesetting industry. Lorem Ipsum has been the industry's standard dummy text ever since the 1500s, when an unknown printer took a galley of type and scrambled it to make a type specimen book. It has survived not only five centuries, but also the leap into electronic typesetting, remaining essentially unchanged. It was popularised in the 1960s</p>
  <div class="btn btn-blue" style="left:976px;top:1455px;width:146px;height:56px">Read More</div>
</section>

<!-- free consult band -->
<section class="abs band">
  <div class="abs" style="left:160px;top:30px;font-size:35px;font-weight:900;color:var(--orange);text-align:right;line-height:1.15;width:200px">Get A Free Consult</div>
  <div class="abs" style="left:396px;top:26px;width:3px;height:96px;background:#fff"></div>
  <div class="abs" style="left:414px;top:56px;font-size:26px;color:#fff;white-space:nowrap">We love help you to grow your business</div>
  <div class="btn btn-orange" style="left:944px;top:46px;width:178px;height:56px">Register Now</div>
</section>

<!-- services gallery -->
<section>
  <div class="rule" style="left:78px;top:1822px"></div>
  <h2 class="abs h2" style="left:78px;top:1834px;color:var(--blue)">Our Services</h2>
  <p class="abs txt" style="left:78px;top:1896px;width:300px">Lorem Ipsum is simply dummy text of the printing and typesetting industry.</p>
  <div class="ph" role="img" aria-label="Colleagues reviewing a document" style="left:78px;top:2003px;width:332px;height:258px;background:linear-gradient(135deg,#eef0f2,#a9b2bd)"></div>
  <div class="ph" role="img" aria-label="Team meeting in an office" style="left:78px;top:2285px;width:332px;height:188px;background:linear-gradient(135deg,#dde4ec,#8d9aab)"></div>
  <div class="ph" role="img" aria-label="Hands over a tablet and papers" style="left:434px;top:1899px;width:330px;height:312px;background:linear-gradient(135deg,#f2f2f2,#b6bec8)"></div>
  <div class="ph" role="img" aria-label="Business people talking in a hallway" style="left:434px;top:2235px;width:330px;height:238px;background:linear-gradient(135deg,#cfd5dc,#6f7884)"></div>
  <div class="ph" role="img" aria-label="Two businessmen shaking hands" style="left:790px;top:1826px;width:332px;height:312px;background:linear-gradient(135deg,#e6e8ea,#8f98a3)"></div>
  <div class="ph" role="img" aria-label="Handshake at a business meeting" style="left:790px;top:2168px;width:332px;height:305px;background:linear-gradient(135deg,#e3e6e9,#79828e)"></div>
</section>

<!-- experience pill -->
<section>
  <div class="abs" style="left:0;top:2610px;width:1200px;height:3px;background:var(--blue)"></div>
  <div class="abs" style="left:78px;top:2550px;width:1044px;height:122px;border-radius:61px;background:var(--blue)"></div>
  <div class="abs" style="left:112px;top:2596px;font-size:24px;color:#fff;white-space:nowrap">Year of Experience we'll ensure you always get the best Guidance.</div>
  <div class="btn btn-orange" style="left:905px;top:2580px;width:178px;height:58px">Get A Quote</div>
</section>

<!-- recent news -->
<section>
  <div class="ph" role="img" aria-label="Smiling office team at a desk" style="left:78px;top:2745px;width:332px;height:218px;background:linear-gradient(135deg,#7b6a5c,#c7b9a8 50%,#4f4a48)"></div>
  <div class="card-date" style="left:78px;top:2773px">15 <small style="font-weight:400;font-size:14px">May</small></div>
  <div class="abs news-title" style="left:78px;top:2982px">Loremprinting typesetting industry.</div>
  <div class="abs" style="left:78px;top:3016px;font-size:12px;color:var(--muted)">Posted by <b style="color:var(--ink)">Dana Orwell</b></div>
  <p class="abs txt" style="left:78px;top:3050px;width:320px;font-size:14px">Lorem Ipsum is simply dummy text of the text has been the industry's standard dummy text.</p>
  <div class="abs readmore" style="left:78px;top:3120px;border-bottom:1px solid #333">Read More &raquo;</div>

  <div class="ph" role="img" aria-label="Business people discussing papers" style="left:434px;top:2745px;width:330px;height:218px;background:linear-gradient(135deg,#e2e5e9,#7e8792)"></div>
  <div class="card-date" style="left:434px;top:2773px">15 <small style="font-weight:400;font-size:14px">May</small></div>
  <div class="abs news-title" style="left:434px;top:2982px">Loremprinting typesetting industry.</div>
  <div class="abs" style="left:434px;top:3016px;font-size:12px;color:var(--muted)">Posted by <b style="color:var(--ink)">Dana Orwell</b></div>
  <p class="abs txt" style="left:434px;top:3050px;width:320px;font-size:14px">Lorem Ipsum is simply dummy text of the text has been the industry's standard dummy text.</p>
  <div class="abs readmore" style="left:434px;top:3120px;border-bottom:1px solid #333">Read More &raquo;</div>

  <div class="rule" style="left:1060px;top:2742px"></div>
  <h2 class="abs h2" style="right:78px;top:2755px;color:var(--orange)">Recent News</h2>
  <p class="abs txt" style="right:78px;top:2818px;width:320px;text-align:right">Lorem Ipsum is simply dummy text of the printing and typesetting industry. Lorem Ipsum has been the industry's standard dummy text ever since the 1500s.</p>
  <div class="btn btn-blue" style="left:976px;top:2950px;width:146px;height:56px">Read More</div>
</section>

<!-- request a call back -->
<section class="abs callback">
  <div class="rule" style="left:78px;top:58px;background:#fff"></div>
  <h2 class="abs h2" style="left:78px;top:70px;color:#fff">Request A Call back</h2>
  <p class="abs" style="left:78px;top:132px;width:320px;font-size:14.5px;line-height:1.7;color:#fff">Lorem Ipsum is simply dummy text of the printing and typesetting industry.</p>
  <div class="field" style="left:527px;top:64px;width:294px">Name :</div>
  <div class="field" style="left:829px;top:64px;width:293px">Email</div>
  <div class="field" style="left:527px;top:132px;width:294px">Phone :</div>
  <div class="field" style="left:829px;top:132px;width:293px">I would like to discuss :<span style="position:absolute;right:14px">&#9662;</span></div>
  <div class="btn btn-orange" style="left:527px;top:200px;width:158px;height:54px">Submit Now</div>
</section>

<!-- happy clients -->
<section>
  <div class="rule" style="left:569px;top:3620px"></div>
  <h2 class="abs h2" style="left:0;width:1200px;text-align:center;top:3630px;color:var(--orange)">Our Happy Clients</h2>
  <p class="abs txt" style="left:0;width:1200px;text-align:center;top:3700px">Lorem Ipsum is simply dummy text of the printing and typesetting industry.<br>Lorem Ipsum has been the industry's standard dummy text ever since the 1500s.</p>

  <div class="abs" style="left:30px;top:3846px;width:38px;height:38px;background:var(--orange)"><svg width="38" height="38"><path d="M23 12l-8 7 8 7" fill="#fff"/></svg></div>
  <div class="abs" style="left:1132px;top:3846px;width:38px;height:38px;background:var(--blue)"><svg width="38" height="38"><path d="M15 12l8 7-8 7" fill="#fff"/></svg></div>

  <div class="quote" style="left:78px;top:3785px"><span class="q">&ldquo;</span>Lorem Ipsum is simply dummy text of the printing and typesetting industry. Lorem Ipsum has been the industry's standard dummy text ever since the 1500s</div>
  <div class="avatar" role="img" aria-label="Client portrait" style="left:78px;top:3975px"></div>
  <div class="cname" style="left:194px;top:3995px">Lena Varga</div>
  <div class="crole" style="left:194px;top:4030px">Company Manager</div>

  <div class="quote" style="left:440px;top:3785px"><span class="q">&ldquo;</span>Lorem Ipsum is simply dummy text of the printing and typesetting industry. Lorem Ipsum has been the industry's standard dummy text ever since the 1500s</div>
  <div class="avatar" role="img" aria-label="Client portrait" style="left:440px;top:3975px"></div>
  <div class="cname" style="left:556px;top:3995px">Lena Varga</div>
  <div class="crole" style="left:556px;top:4030px">Company Manager</div>

  <div class="quote" style="left:800px;top:3785px"><span class="q">&ldquo;</span>Lorem Ipsum is simply dummy text of the printing and typesetting industry. Lorem Ipsum has been the industry's standard dummy text ever since the 1500s</div>
  <div class="avatar" role="img" aria-label="Client portrait" style="left:800px;top:3975px"></div>
  <div class="cname" style="left:916px;top:3995px">Lena Varga</div>
  <div class="crole" style="left:916px;top:4030px">Company Manager</div>
</section>

<!-- footer -->
<footer class="abs footer">
  <div class="abs" style="left:78px;top:55px;display:flex;align-items:center;gap:10px">
    <div style="width:36px;height:36px;background:#fff"></div>
    <div style="font-size:21px;font-weight:900;color:#fff;letter-spacing:1px;white-space:nowrap">MARENDO ADVISERS</div>
  </div>
  <p class="abs" style="left:78px;top:125px;width:250px;font-size:14px;line-height:1.75;color:#eee">Lorem Ipsum is simply dummy text of industry. Lorem Ipsum has been the industry's standard dummy text ever since the 1500s</p>
  <div class="social" style="left:78px;top:250px">
    <span style="width:44px;height:44px;background:var(--orange)"></span>
    <span style="width:44px;height:44px;background:#fff"></span>
    <span style="width:44px;height:44px;background:#fff"></span>
    <span style="width:44px;height:44px;background:#fff"></span>
  </div>

  <h4 style="left:408px;top:58px">Navigation</h4>
  <div class="col" style="left:408px;top:100px">Home<br>About<br>Services<br>Portfolio<br>Contact Us</div>

  <h4 style="left:573px;top:58px">Get In Touch</h4>
  <div class="abs" style="left:573px;top:104px;width:34px;height:34px;border-radius:50%;background:var(--orange)"><svg width="34" height="34"><path d="M17 8a6 6 0 0 0-6 6c0 5 6 12 6 12s6-7 6-12a6 6 0 0 0-6-6z" fill="#fff"/><circle cx="17" cy="14" r="2.2" fill="#f7a11a"/></svg></div>
  <div class="abs" style="left:620px;top:100px;font-size:14px;line-height:1.5;color:#eee"><b style="font-size:17px;color:#fff">Marendo Adviser</b><br>27 Cedar Run Lane<br>Halden, Ohio 44012</div>
  <div class="abs" style="left:573px;top:196px;width:34px;height:34px;border-radius:50%;background:var(--orange)"><svg width="34" height="34" viewBox="-5 -5 34 34"><path fill="#fff" d="M6.6 10.8a15 15 0 0 0 6.6 6.6l2.2-2.2c.3-.3.7-.4 1-.2 1.1.4 2.3.6 3.6.6.6 0 1 .4 1 1V20c0 .6-.4 1-1 1A17 17 0 0 1 3 4c0-.6.4-1 1-1h3.5c.6 0 1 .4 1 1 0 1.3.2 2.5.6 3.6.1.3 0 .7-.2 1z"/></svg></div>
  <div class="abs" style="left:620px;top:204px;font-size:15px;color:#eee">555-014-2790</div>
  <div class="abs" style="left:573px;top:260px;width:34px;height:34px;border-radius:50%;background:var(--orange)"><svg width="34" height="34"><rect x="9" y="11" width="16" height="12" fill="#fff"/><path d="M9 11l8 6 8-6" stroke="#f7a11a" stroke-width="1.5" fill="none"/></svg></div>
  <div class="abs" style="left:620px;top:268px;font-size:15px;color:#eee">hello@marendo-advisers.com</div>

  <h4 style="left:875px;top:58px">Newsletter</h4>
  <p class="abs" style="left:875px;top:98px;width:250px;font-size:14px;line-height:1.6;color:#eee">Would you like to receive exclusive access to articles, white papers and our regular monthly newsletter?</p>
  <div class="abs" style="left:875px;top:190px;width:247px;height:50px;background:#fff;color:#888;font-size:14px;padding:16px 10px">Enter Email id</div>
  <div class="btn btn-orange" style="left:875px;top:254px;width:158px;height:56px;border-radius:0">Submit</div>
</footer>
<div class="abs bottombar">&copy; 2018 &nbsp;MARENDO ADVISERS . All rights reserved.</div>

</body>
</html>
```